Specialty Contact lens for children

We need a large size canvas 24x36" to advertise specialty fit contact lens for children to control myopia. please visit our website for more about our office theme www.tarnobelle.com
We want modern , fresh, happy design. Color blue, green, white. Final design should communicate the best lens choice for the children. Banner to include a picture of happy teen playing sports or out in park without glasses. To portray the new ability to see without glasses.
ORTHO-K #1 MYOPIA control treatment for children
- Corrects your vision while you sleep
- Creates crisp clear vision all day
- Freedom: No glasses, No Surgery, No soft lenses
-Safe and effective for children and adults

Target Market(s)

8-25 years old

Industry/Entity Type

Health Care

Font styles to use
Sans Serif

Colors
0692cd
cee9f5
ecf7fb
ffffff
86cfc6

Requirements
Must have
• Picture of teen playing sports or outdoors without glasses
Nice to have
• office logo on banner. happy color blue, green, white.
• Modern font: century gothic

```html
<!DOCTYPE html>
<html lang="en">
<head>
<meta charset="utf-8">
<title>Ortho-K Myopia Control Poster</title>
<link rel="stylesheet" href="https://fonts.googleapis.com/css2?family=Montserrat:wght@600&family=Questrial&display=swap">
<style>
  :root {
    --brand-blue: #0692cd;
    --water-deep: #1b9fdc;
    --water-light: #7ccdf0;
    --ice: #cee9f5;
    --mist: #ecf7fb;
    --white: #ffffff;
    --teal: #86cfc6;
    --teal-text: #45b8b0;
    --band-teal: #4fbcb5;
    --mark-gold: #f2c230;
    --mark-grey: #5a5a5a;
  }
  html, body {
    margin: 0;
    padding: 0;
    overflow: hidden;
    background: var(--white);
  }
  .poster {
    position: relative;
    width: 800px;
    height: 1200px;
    overflow: hidden;
    background: var(--white);
    font-family: "Questrial", "Century Gothic", sans-serif;
  }
  .hero-photo {
    position: absolute;
    left: 0;
    top: 0;
    width: 800px;
    height: 560px;
    background:
      linear-gradient(to bottom, rgba(255,255,255,0) 60%, var(--white) 100%),
      linear-gradient(170deg, var(--water-deep) 0%, #3fb0e6 40%, var(--water-light) 75%, var(--ice) 100%);
  }
  .title {
    position: absolute;
    left: 40px;
    top: 400px;
    margin: 0;
    font-family: "Montserrat", "Century Gothic", sans-serif;
    font-weight: 600;
    font-size: 90px;
    line-height: 1;
    letter-spacing: 1px;
    color: var(--brand-blue);
  }
  .tagline-band {
    position: absolute;
    left: 42px;
    top: 506px;
    width: 720px;
    height: 45px;
    background: linear-gradient(to right, var(--band-teal) 0%, var(--band-teal) 55%, rgba(134,207,198,0.6) 85%, rgba(134,207,198,0) 100%);
  }
  .tagline {
    position: absolute;
    left: 56px;
    top: 506px;
    margin: 0;
    font-size: 30px;
    line-height: 45px;
    color: var(--white);
  }
  .headline {
    position: absolute;
    left: 42px;
    top: 566px;
    margin: 0;
    font-size: 54px;
    line-height: 60px;
    font-weight: 400;
    color: var(--brand-blue);
  }
  .benefits {
    position: absolute;
    left: 43px;
    top: 706px;
    margin: 0;
    padding: 0;
    list-style: none;
    font-size: 25px;
    line-height: 37px;
    color: var(--teal-text);
  }
  .accent-lines {
    position: absolute;
    left: 0;
    top: 900px;
  }
  .cta {
    position: absolute;
    left: 43px;
    top: 1128px;
    margin: 0;
    font-size: 25px;
    line-height: 36px;
    color: var(--brand-blue);
  }
  .practice-mark {
    position: absolute;
    left: 598px;
    top: 944px;
    width: 164px;
    text-align: center;
  }
  .practice-mark .mark-square {
    display: block;
    width: 118px;
    height: 150px;
    margin: 0 0 14px 22px;
    background: var(--mark-gold);
  }
  .practice-name {
    margin: 0;
    font-size: 22px;
    line-height: 22px;
    letter-spacing: 1px;
    color: var(--mark-grey);
  }
</style>
</head>
<body>
<main class="poster">
  <div class="hero-photo" role="img" aria-label="Happy mother and two daughters swimming underwater in a bright blue pool without glasses"></div>

  <h1 class="title">ORTHO-K</h1>
  <div class="tagline-band"></div>
  <p class="tagline">#1 myopia control treatment for children</p>

  <h2 class="headline">NO GLASSES, NO SURGERY,<br>NO DAYTIME LENSES.</h2>

  <ul class="benefits">
    <li>Prevents your nearsighted from getting worse</li>
    <li>Corrects your vision while you sleep</li>
    <li>Creates crisp clear vision all day</li>
    <li>Safe and effective for children and adults</li>
    <li>Prevents your child’s nearsightedness from getting worse</li>
  </ul>

  <svg class="accent-lines" width="800" height="260" viewBox="0 0 800 260" aria-hidden="true">
    <defs>
      <linearGradient id="lineFade" x1="0" y1="0" x2="1" y2="0">
        <stop offset="0" stop-color="#86cfc6" stop-opacity="0.9"/>
        <stop offset="1" stop-color="#86cfc6" stop-opacity="0"/>
      </linearGradient>
    </defs>
    <line x1="0" y1="24" x2="520" y2="190" stroke="url(#lineFade)" stroke-width="5"/>
    <line x1="0" y1="56" x2="500" y2="220" stroke="url(#lineFade)" stroke-width="3"/>
  </svg>

  <p class="cta">Get a free ORTHO-K Consultation today.</p>

  <div class="practice-mark">
    <span class="mark-square"></span>
    <p class="practice-name">TARNOBELLE<br>OPTOMETRY</p>
  </div>
</main>
</body>
</html>
```